Sonvera Listening Wellness Care Mission

Create a one page flyer (dimensions = 12" wide x 8" tall) that will be turned into a sticker for laptops that highlights our mission statement and our Why, How, and What (elements of the Bright Spiral). Additional design direction and content is provided in the attached files.

```html
<!DOCTYPE html>
<html lang="en">
<head>
<meta charset="utf-8">
<title>Sonvera Listening Wellness Care – Mission Sticker</title>
<link href="https://fonts.googleapis.com/css2?family=Open+Sans:wght@600;700;800&family=Carlito:wght@400;700&display=swap" rel="stylesheet">
<style>
  :root {
    --plum: #4b0a5c;
    --crimson: #d2174b;
    --orange: #ee5f2c;
    --sun: #f8b918;
    --gold: #f5a800;
    --paper: #f4f5f7;
    --ink: #3a3a3c;
    --line: #b9bbc0;
    --stage: #e6e6e8;
  }
  * { box-sizing: border-box; margin: 0; padding: 0; }
  html, body { width: 1200px; height: 910px; overflow: hidden; background: var(--stage); }
  .sticker {
    position: absolute; left: 30px; top: 73px;
    width: 1140px; height: 764px;
    background: var(--paper);
    font-family: "Carlito", "Calibri", sans-serif;
    color: var(--ink);
  }
  .sticker-graphics { position: absolute; inset: 0; width: 1140px; height: 764px; }
  .mission-title {
    position: absolute; top: 46px; left: 0; width: 100%;
    text-align: center; color: var(--sun);
    font-family: "Open Sans", sans-serif; font-weight: 700; font-size: 26px;
  }
  .mission-text {
    position: absolute; top: 110px; left: 80px; right: 80px;
    text-align: center; color: #fff; font-size: 18.5px; line-height: 1.3;
  }
  .question-pill {
    position: absolute; left: 20px; width: 349px; height: 48px;
    border: 3px solid #fff; border-radius: 24px;
    box-shadow: 0 2px 5px rgba(0,0,0,.18);
    display: flex; align-items: center; justify-content: center; text-align: center;
    color: #fff; font-family: "Open Sans", sans-serif; font-weight: 700;
    font-size: 16px; line-height: 1.1;
  }
  .pill-how { top: 325px; background: var(--orange); }
  .pill-why { top: 447px; background: #c61f4b; }
  .pill-what { top: 570px; background: var(--sun); }
  .core-word {
    position: absolute; left: 498px; top: 442px; width: 148px; text-align: center;
    color: #fff; font-family: "Open Sans", sans-serif; font-weight: 800; font-size: 40px;
  }
  .answer { position: absolute; left: 782px; width: 330px; font-size: 14.5px; line-height: 1.3; }
  .answer h3 { font-family: "Open Sans", sans-serif; font-weight: 700; font-size: 16.5px; margin-bottom: 1px; }
  .answer-how { top: 318px; } .answer-how h3 { color: var(--orange); }
  .answer-why { top: 446px; } .answer-why h3 { color: var(--crimson); }
  .answer-what { top: 562px; } .answer-what h3 { color: var(--gold); }
  .brand-name {
    position: absolute; right: 26px; top: 714px;
    display: flex; align-items: center; gap: 7px;
    color: var(--plum); font-family: "Carlito", "Calibri", sans-serif; font-weight: 400; font-size: 18px;
  }
  .brand-dot { width: 9px; height: 9px; border-radius: 50%; background: var(--plum); }
</style>
</head>
<body>
<main class="sticker">
  <svg class="sticker-graphics" viewBox="0 0 1140 764" aria-hidden="true">
    <defs>
      <linearGradient id="headerGrad" x1="0" x2="1">
        <stop offset="0" stop-color="#4b0a5c"/>
        <stop offset="0.5" stop-color="#9a1458"/>
        <stop offset="1" stop-color="#d8174a"/>
      </linearGradient>
      <linearGradient id="ruleGrad" x1="0" x2="1">
        <stop offset="0" stop-color="#4b0a5c"/>
        <stop offset="1" stop-color="#d8174a"/>
      </linearGradient>
      <radialGradient id="outerGrad" cx="0.5" cy="0.5" r="0.5">
        <stop offset="0.75" stop-color="#f4a11f"/>
        <stop offset="0.88" stop-color="#fbc21b"/>
        <stop offset="1" stop-color="#f8b316"/>
      </radialGradient>
      <linearGradient id="ringGrad" x1="0" x2="1">
        <stop offset="0" stop-color="#cf1a4c"/>
        <stop offset="1" stop-color="#ef5e2c"/>
      </linearGradient>
      <linearGradient id="coreGrad" x1="0" x2="1">
        <stop offset="0" stop-color="#560c5e"/>
        <stop offset="1" stop-color="#d81a4b"/>
      </linearGradient>
    </defs>
    <path d="M0 217 L570 250 L1140 217 L1140 226 L570 262 L0 226 Z" fill="var(--sun)"/>
    <path d="M0 0 H1140 V217 L570 250 L0 217 Z" fill="url(#headerGrad)"/>

    <g stroke="var(--line)" stroke-width="1.3" fill="none">
      <polyline points="369,349 420,349 507,402"/>
      <polyline points="369,471 510,471"/>
      <polyline points="369,613 420,613 465,566"/>
      <polyline points="659,402 720,349 772,349"/>
      <polyline points="643,471 772,471"/>
      <polyline points="681,566 720,596 772,596"/>
    </g>

    <circle cx="572" cy="471" r="121" fill="url(#outerGrad)"/>
    <circle cx="572" cy="471" r="95" fill="url(#ringGrad)" stroke="#fff" stroke-width="1.5"/>
    <circle cx="572" cy="471" r="74" fill="url(#coreGrad)" stroke="#fff" stroke-width="1.5"/>

    <g fill="#c4c5c9">
      <circle cx="507" cy="402" r="5"/>
      <circle cx="510" cy="471" r="5"/>
      <circle cx="465" cy="566" r="5"/>
      <circle cx="659" cy="402" r="5"/>
      <circle cx="643" cy="471" r="5"/>
      <circle cx="681" cy="566" r="5"/>
    </g>

    <rect x="29" y="701" width="1087" height="7" fill="url(#ruleGrad)"/>
  </svg>

  <h1 class="mission-title">MISSION STATEMENT</h1>
  <p class="mission-text">Hearing health care is complicated. We make it easy by connecting organizations and their customers with quality care, superior products, and an exceptional service experience. Because we believe that everyone deserves to hear well and live happy.</p>

  <div class="question-pill pill-how">How Do You Do / What You Do?</div>
  <div class="question-pill pill-why">Why Do You Do What You Do?<br>What’s the purpose?</div>
  <div class="question-pill pill-what">What Do You Do?</div>

  <div class="core-word">WHY?</div>

  <section class="answer answer-how">
    <h3>Our How:</h3>
    <p>We make hearing health care simple. We help people navigate the hearing health care journey. We deliver more value.</p>
  </section>
  <section class="answer answer-why">
    <h3>Our Why:</h3>
    <p>We connect people and resources to improve the lives of people affected by hearing loss.</p>
  </section>
  <section class="answer answer-what">
    <h3>OurWhat:</h3>
    <p>We partner with organizations to deliver hearing benefits to their customers.</p>
  </section>

  <div class="brand-name"><span class="brand-dot"></span>Sonvera</div>
</main>
</body>
</html>
```